Invest in Real Estate housing and apartment development projects in Lima - Peru

Need a presentation for Grupo Velmira, a top Real Estate developer from Peru who is looking for new leading investors such as Top Regional and Worldwide Real Estate funds and Regional Family offices and High Networth individuals to invest in Real Estate projects developed by/with Grupo Velmira. Velmira is focused on middle income apartments (housing) and has developed and delivered aprox 1400 apartments, and is currently developing and building 400 apartments. Velmira currently has a potential to develop 1500 more apartments. And is looking to raise between US $50 and 60mm dollars a year in additional new investments, all focused on real estate housing (essentially vertical housing, apartments)
I have already some information and slides prepared with information regarding management fees, development and sales/marketing fees, success fees which are alligned to IRR of the project.

Target Market(s)

Real Estate investors in Latin America

Industry/Entity Type

Real Estate Development

Colors

Designer to choose colors to be used in the design.

Requirements
Must have
• Graphs and pictures of real estate projects. Data of housing market from Lima, capital of Peru compared to other top capitals in South America

```html
<!DOCTYPE html>
<html lang="en">
<head>
<meta charset="utf-8">
<title>Grupo Velmira — Investor Presentation Template</title>
<link href="https://fonts.googleapis.com/css2?family=Open+Sans:wght@400;600;700;800&display=swap" rel="stylesheet">
<style>
:root{
  --green:#8cc63f;
  --green-deep:#6ea42c;
  --green-pale:#dcefc4;
  --brown:#3b2e27;
  --brown-soft:#5a4a40;
  --grey:#f2f2f2;
  --grey-mid:#d9d9d9;
  --grey-dark:#bdbdbd;
  --ink:#3a3a3a;
  --muted:#9a9a9a;
  --white:#ffffff;
  --page:#e6e6e6;
}
*{box-sizing:border-box;margin:0;padding:0}
html,body{width:1200px;height:4572px;overflow:hidden}
body{background:var(--page);font-family:"Open Sans",Arial,sans-serif;color:var(--ink)}
.deck{display:grid;grid-template-columns:repeat(3,396px);grid-template-rows:repeat(20,1fr);gap:6px;width:1200px;height:4572px}
.slide{position:relative;overflow:hidden;background:var(--white);font-size:6px}
.slide--grey{background:var(--grey)}
.slide--green{background:var(--green)}
.slide--brown{background:var(--brown)}
.abs{position:absolute}
.slide-title{position:absolute;left:16px;top:12px;font-size:10px;font-weight:700;text-transform:uppercase;letter-spacing:.3px;color:var(--ink)}
.slide-title--case{text-transform:none;font-weight:600;font-size:10px}
.slide-title--light{color:var(--white)}
.brand-foot{position:absolute;left:14px;bottom:7px;display:flex;align-items:center;gap:3px;font-size:6px;font-weight:700;color:var(--green)}
.brand-foot::before{content:"";width:5px;height:5px;background:var(--green)}
.brand-foot--light{color:var(--white)}
.brand-foot--light::before{background:var(--white)}
.note{font-size:5px;line-height:1.55;color:var(--muted)}
.note--light{color:#e8e8e8}
.label{font-size:6.5px;font-weight:700;color:var(--ink);text-transform:uppercase}
.label--light{color:var(--white)}
.label--green{color:var(--green)}
.big-stat{font-weight:800;color:var(--green)}
.photo{position:absolute;background:linear-gradient(135deg,#b9c4b0 0%,#8b9a86 55%,#6c7769 100%)}
.photo--warm{background:linear-gradient(135deg,#e4d7c8 0%,#c2a990 60%,#8c7460 100%)}
.photo--sky{background:linear-gradient(180deg,#cfe0ee 0%,#d9e4d2 55%,#8fa27f 100%)}
.photo--dark{background:linear-gradient(135deg,#5d5048 0%,#3b2e27 100%)}
.photo--green{background:linear-gradient(135deg,#a9d46e 0%,#6ea42c 100%)}
.photo--soft{background:linear-gradient(180deg,rgba(217,217,217,.15) 0%,rgba(189,189,189,.55) 100%)}
.photo--round{border-radius:50%}
.tint-brown{position:absolute;background:rgba(59,46,39,.78)}
.tint-green{position:absolute;background:rgba(140,198,63,.85)}
.box-green{position:absolute;background:var(--green)}
.box-brown{position:absolute;background:var(--brown)}
.dot{display:inline-block;width:9px;height:9px;border-radius:50%;background:var(--green);flex:none}
.row{display:flex;align-items:center;gap:5px}
.logo-lockup{position:absolute;display:flex;align-items:center;gap:7px}
.logo-lockup .logo-square{width:22px;height:22px;background:var(--green)}
.logo-name{font-weight:800;color:var(--green);font-size:24px;letter-spacing:.5px;line-height:1}
.tagline{display:block;font-size:6px;color:var(--muted);letter-spacing:1px;margin-top:3px;text-transform:uppercase}
.divider-heading{font-size:14px;font-weight:800;text-transform:uppercase;color:var(--white);letter-spacing:.4px}
.chip{position:absolute;width:22px;height:14px;background:var(--green);color:var(--white);font-size:7px;font-weight:700;display:flex;align-items:center;justify-content:center}
.table{position:absolute;border-collapse:collapse;font-size:5px;color:var(--ink)}
.table th{background:var(--brown);color:var(--white);font-weight:600;padding:3px 5px;text-align:left}
.table td{padding:3px 5px;border-bottom:1px solid var(--grey-mid)}
.table tr:nth-child(even) td{background:var(--grey)}
.price-col{position:absolute;top:50px;width:92px;height:150px;background:var(--grey);text-align:center}
.price-col header{background:var(--green);color:var(--white);font-weight:700;font-size:7px;padding:6px 0}
.price-col .amount{font-size:16px;font-weight:800;color:var(--brown);margin:8px 0 4px}
.price-col p{font-size:5px;color:var(--muted);line-height:2}
.ground{position:absolute;left:0;bottom:0;width:396px;height:30px;background:var(--brown)}
.ground--green{background:var(--green)}
.ground-legend{position:absolute;left:16px;right:16px;bottom:9px;display:flex;justify-content:space-between;font-size:5.5px;color:var(--white);font-weight:600}
.stat-block{position:absolute;width:70px}
.stat-block b{display:block;font-size:11px;font-weight:800;color:var(--green);line-height:1.1}
.stat-block span{font-size:5px;color:var(--muted);line-height:1.4}
.meter{height:4px;background:var(--grey-mid);margin-top:3px}
.meter i{display:block;height:4px;background:var(--green)}
svg{display:block}
svg text{font-family:"Open Sans",Arial,sans-serif}
</style>
</head>
<body>
<main class="deck">

<!-- row 1 -->
<section class="slide">
  <div class="logo-lockup" style="left:96px;top:88px">
    <span class="logo-square"></span>
    <div><span class="logo-name">GRUPO VELMIRA</span><span class="tagline">Homes for every family</span></div>
  </div>
</section>

<section class="slide">
  <div class="photo photo--warm" style="left:150px;top:0;width:246px;height:160px" role="img" aria-label="Family relaxing together at home"></div>
  <div class="box-green" style="left:0;top:160px;width:396px;height:6px"></div>
  <div class="abs" style="left:18px;top:60px;width:120px">
    <div class="label label--green" style="font-size:8px">Velmira</div>
    <div style="font-size:15px;font-weight:800;color:var(--ink);margin-top:4px">Your Title Here</div>
    <p class="note" style="margin-top:4px">Housing projects built for growing families in Lima.</p>
  </div>
  <span class="brand-foot">VELMIRA</span>
</section>

<section class="slide slide--green">
  <div class="photo photo--warm" style="left:0;top:90px;width:130px;height:133px" role="img" aria-label="Couple in a new apartment"></div>
  <div class="photo photo--sky" style="left:134px;top:90px;width:130px;height:133px" role="img" aria-label="Apartment building exterior"></div>
  <div class="photo" style="left:268px;top:90px;width:128px;height:133px" role="img" aria-label="Family in a living room"></div>
  <div class="abs divider-heading" style="right:22px;top:34px">Your Title Goes Here</div>
</section>

<!-- row 2 -->
<section class="slide">
  <div class="slide-title">Our Agenda</div>
  <div class="chip" style="left:24px;top:48px">01</div><div class="abs label" style="left:52px;top:51px">Company Profile</div>
  <div class="chip" style="left:24px;top:82px">02</div><div class="abs label" style="left:52px;top:85px">Projects Delivered</div>
  <div class="chip" style="left:24px;top:116px">03</div><div class="abs label" style="left:52px;top:119px">Lima Housing Market</div>
  <div class="chip" style="left:24px;top:150px">04</div><div class="abs label" style="left:52px;top:153px">Fee Structure</div>
  <div class="chip" style="left:210px;top:48px">05</div><div class="abs label" style="left:238px;top:51px">Pipeline</div>
  <div class="chip" style="left:210px;top:82px">06</div><div class="abs label" style="left:238px;top:85px">Investor Returns</div>
  <div class="chip" style="left:210px;top:116px">07</div><div class="abs label" style="left:238px;top:119px">Team</div>
  <div class="chip" style="left:210px;top:150px">08</div><div class="abs label" style="left:238px;top:153px">Contact</div>
  <span class="brand-foot">VELMIRA</span>
</section>

<section class="slide">
  <div class="slide-title">Bullets Point's Level</div>
  <div class="abs" style="left:24px;top:44px;width:350px;display:grid;gap:9px">
    <div class="row"><span class="dot"></span><span class="label">Middle income apartments</span></div>
    <div class="row" style="padding-left:16px"><span class="dot" style="width:6px;height:6px"></span><span class="note">Vertical housing for families across Lima districts.</span></div>
    <div class="row"><span class="dot"></span><span class="label">1,400 apartments delivered</span></div>
    <div class="row" style="padding-left:16px"><span class="dot" style="width:6px;height:6px"></span><span class="note">All projects completed and handed over on schedule.</span></div>
    <div class="row"><span class="dot"></span><span class="label">400 apartments in construction</span></div>
    <div class="row"><span class="dot"></span><span class="label">1,500 apartments in pipeline</span></div>
  </div>
  <span class="brand-foot">VELMIRA</span>
</section>

<section class="slide">
  <div class="photo photo--sky" style="left:0;top:0;width:132px;height:110px" role="img" aria-label="Residential tower"></div>
  <div class="photo photo--warm" style="left:134px;top:0;width:130px;height:110px" role="img" aria-label="Family portrait at home"></div>
  <div class="photo" style="left:266px;top:0;width:130px;height:110px" role="img" aria-label="Modern kitchen interior"></div>
  <div class="box-green" style="left:0;top:112px;width:132px;height:111px"></div>
  <div class="photo photo--warm" style="left:134px;top:112px;width:130px;height:111px" role="img" aria-label="Children playing in a park"></div>
  <div class="photo photo--sky" style="left:266px;top:112px;width:130px;height:111px" role="img" aria-label="Apartment balcony view"></div>
  <div class="abs label label--light" style="left:14px;top:160px">Our Projects</div>
</section>

<!-- row 3 -->
<section class="slide">
  <div class="slide-title">Your Title Here</div>
  <div class="photo photo--sky" style="left:16px;top:44px;width:150px;height:150px" role="img" aria-label="Apartment complex under blue sky"></div>
  <div class="box-green" style="left:184px;top:46px;width:30px;height:3px"></div>
  <div class="abs" style="left:184px;top:56px;width:190px">
    <div class="label">Building value for investors</div>
    <p class="note" style="margin-top:6px">Grupo Velmira develops and sells middle income apartments in Lima, with a track record of delivering every project on time and within budget.</p>
    <p class="note" style="margin-top:6px">Our pipeline offers investors steady returns aligned with project IRR.</p>
  </div>
  <span class="brand-foot">VELMIRA</span>
</section>

<section class="slide">
  <svg class="abs" style="left:186px;top:64px" width="24" height="24" viewBox="0 0 24 24"><path d="M3 12 L12 4 L21 12 V21 H3 Z" fill="var(--green)"/></svg>
  <div class="abs" style="left:0;right:0;top:98px;text-align:center;font-size:15px;font-weight:800;color:var(--ink)">DIVIDER PAGE</div>
  <div class="box-green" style="left:178px;top:124px;width:40px;height:3px"></div>
  <span class="brand-foot">VELMIRA</span>
</section>

<section class="slide">
  <div class="slide-title">Text &amp; Bullet Area</div>
  <div class="abs" style="left:24px;top:50px;width:350px;display:grid;grid-template-columns:1fr 1fr;gap:22px 18px">
    <div class="row"><span class="dot" style="width:16px;height:16px"></span><div><div class="label">Location</div><p class="note">Prime districts of Lima</p></div></div>
    <div class="row"><span class="dot" style="width:16px;height:16px"></span><div><div class="label">Design</div><p class="note">Efficient family layouts</p></div></div>
    <div class="row"><span class="dot" style="width:16px;height:16px"></span><div><div class="label">Financing</div><p class="note">Bank mortgage partners</p></div></div>
    <div class="row"><span class="dot" style="width:16px;height:16px"></span><div><div class="label">Sales</div><p class="note">In-house marketing team</p></div></div>
    <div class="row"><span class="dot" style="width:16px;height:16px"></span><div><div class="label">Delivery</div><p class="note">On time, every project</p></div></div>
    <div class="row"><span class="dot" style="width:16px;height:16px"></span><div><div class="label">Returns</div><p class="note">Fees aligned to IRR</p></div></div>
  </div>
  <span class="brand-foot">VELMIRA</span>
</section>

<!-- row 4 -->
<section class="slide">
  <div class="abs" style="left:20px;top:20px;display:grid;grid-template-columns:repeat(4,80px);gap:16px 14px">
    <span style="height:22px;background:var(--green-pale);border-radius:11px"></span>
    <span style="height:22px;background:var(--grey-mid)"></span>
    <span style="height:22px;background:var(--green-pale)"></span>
    <span style="height:22px;background:var(--grey-mid);border-radius:11px"></span>
    <span style="height:22px;background:var(--grey-mid)"></span>
    <span></span><span></span>
    <span style="height:22px;background:var(--green-pale);border-radius:11px"></span>
    <span style="height:22px;background:var(--green-pale)"></span>
    <span></span><span></span>
    <span style="height:22px;background:var(--grey-mid)"></span>
    <span style="height:22px;background:var(--grey-mid);border-radius:11px"></span>
    <span style="height:22px;background:var(--green-pale)"></span>
    <span style="height:22px;background:var(--grey-mid)"></span>
    <span style="height:22px;background:var(--green-pale);border-radius:11px"></span>
  </div>
  <div class="box-brown" style="left:116px;top:60px;width:164px;height:66px;display:flex;align-items:center;justify-content:center;color:var(--white);font-size:13px;font-weight:600">Our Awesome Client</div>
</section>

<section class="slide slide--brown">
  <div class="box-green" style="left:0;top:0;width:396px;height:70px"></div>
  <div class="abs" style="left:22px;top:60px;width:352px;display:grid;grid-template-columns:repeat(4,1fr);gap:10px;text-align:center">
    <div><div style="width:22px;height:22px;border:2px solid var(--white);border-radius:50%;margin:0 auto 12px;background:var(--brown)"></div><div class="label label--light">Plan</div><p class="note note--light">Land and permits</p></div>
    <div><div style="width:22px;height:22px;border:2px solid var(--white);border-radius:50%;margin:0 auto 12px;background:var(--brown)"></div><div class="label label--light">Design</div><p class="note note--light">Architecture team</p></div>
    <div><div style="width:22px;height:22px;border:2px solid var(--white);border-radius:50%;margin:0 auto 12px;background:var(--brown)"></div><div class="label label--light">Build</div><p class="note note--light">Quality control</p></div>
    <div><div style="width:22px;height:22px;border:2px solid var(--white);border-radius:50%;margin:0 auto 12px;background:var(--brown)"></div><div class="label label--light">Deliver</div><p class="note note--light">Keys to families</p></div>
  </div>
  <span class="brand-foot brand-foot--light">VELMIRA</span>
</section>

<section class="slide">
  <div class="slide-title">Our Mockup Area</div>
  <div class="box-green" style="left:0;top:84px;width:396px;height:70px"></div>
  <div class="photo photo--dark" style="left:130px;top:50px;width:136px;height:90px" role="img" aria-label="Laptop showing the company website"></div>
  <div class="abs" style="left:158px;top:88px;font-size:11px;font-weight:800;color:var(--green)">VELMIRA</div>
  <span class="brand-foot">VELMIRA</span>
</section>

<!-- row 5 -->
<section class="slide">
  <div class="box-brown" style="left:0;top:0;width:110px;height:223px"></div>
  <div class="photo photo--dark" style="left:0;top:0;width:110px;height:110px;opacity:.7" role="img" aria-label="Team meeting"></div>
  <div class="abs label label--light" style="left:14px;top:128px;font-size:9px;line-height:1.3">Group<br>Picture<br>Slide</div>
  <svg class="abs" style="left:130px;top:30px" width="250" height="120" viewBox="0 0 250 120">
    <g fill="var(--green)"><rect x="10" y="60" width="22" height="60"/><rect x="50" y="40" width="22" height="80"/><rect x="90" y="75" width="22" height="45"/><rect x="130" y="20" width="22" height="100"/><rect x="170" y="50" width="22" height="70"/></g>
    <rect x="210" y="30" width="22" height="90" fill="var(--brown)"/>
  </svg>
  <div class="abs big-stat" style="left:170px;top:164px;font-size:22px">+ 85%</div>
  <p class="abs note" style="left:170px;top:194px">Sales growth over five years</p>
</section>

<section class="slide">
  <div class="photo photo--sky" style="left:0;top:0;width:396px;height:223px" role="img" aria-label="Residential building exterior"></div>
  <div class="tint-green" style="left:0;top:0;width:150px;height:223px"></div>
  <div class="abs label label--light" style="left:16px;top:40px;font-size:9px">Your Mockup</div>
  <div class="photo" style="left:196px;top:40px;width:170px;height:110px;background:var(--white);border:6px solid #222" role="img" aria-label="Desktop monitor showing the company brand"></div>
  <div class="abs" style="left:238px;top:86px;font-size:14px;font-weight:800;color:var(--green)">VELMIRA</div>
</section>

<section class="slide slide--brown">
  <div class="slide-title slide-title--light">Our Mockup</div>
  <div class="photo" style="left:170px;top:46px;width:196px;height:120px;background:var(--white);border:6px solid #1c1c1c" role="img" aria-label="Desktop monitor showing the company brand"></div>
  <div class="abs" style="left:222px;top:96px;font-size:16px;font-weight:800;color:var(--green)">VELMIRA</div>
  <p class="abs note note--light" style="left:16px;top:60px;width:130px">Our digital sales platform lets buyers tour apartments online.</p>
  <span class="brand-foot brand-foot--light">VELMIRA</span>
</section>

<!-- row 6 -->
<section class="slide">
  <div class="abs label" style="left:16px;top:60px;font-size:9px;line-height:1.3">This is line<br>chart slide</div>
  <svg class="abs" style="left:120px;top:40px" width="260" height="150" viewBox="0 0 260 150">
    <polyline points="0,110 50,40 100,90 150,30 200,100 250,60" fill="none" stroke="var(--green)" stroke-width="3"/>
    <polyline points="0,60 50,100 100,50 150,110 200,70 250,120" fill="none" stroke="var(--brown)" stroke-width="2"/>
    <line x1="0" y1="140" x2="260" y2="140" stroke="var(--grey-mid)"/>
  </svg>
  <span class="brand-foot">VELMIRA</span>
</section>

<section class="slide">
  <div class="slide-title">Your Title Goes Here</div>
  <div class="photo photo--sky" style="left:16px;top:40px;width:176px;height:70px" role="img" aria-label="Apartment tower"></div>
  <div class="photo" style="left:204px;top:40px;width:176px;height:70px" role="img" aria-label="Townhouses"></div>
  <div class="photo photo--warm" style="left:16px;top:124px;width:176px;height:70px" role="img" aria-label="Living room interior"></div>
  <div class="photo photo--sky" style="left:204px;top:124px;width:176px;height:70px" role="img" aria-label="Residential street"></div>
  <div class="box-green" style="left:16px;top:96px;width:80px;height:14px"></div>
  <div class="box-green" style="left:204px;top:180px;width:80px;height:14px"></div>
  <span class="brand-foot">VELMIRA</span>
</section>

<section class="slide">
  <div class="photo photo--sky" style="left:0;top:0;width:396px;height:223px" role="img" aria-label="Modern apartment building"></div>
  <div class="tint-brown" style="left:220px;top:40px;width:150px;height:140px"></div>
  <div class="abs label label--light" style="left:236px;top:58px;font-size:11px">About Us</div>
  <p class="abs note note--light" style="left:236px;top:80px;width:120px">Grupo Velmira is a Peruvian developer of middle income apartments with 1,400 homes delivered in Lima.</p>
</section>

<!-- row 7 -->
<section class="slide">
  <div class="photo photo--dark" style="left:0;top:0;width:396px;height:223px" role="img" aria-label="City skyline at dusk"></div>
  <div class="tint-brown" style="left:0;top:80px;width:396px;height:56px"></div>
  <div class="abs divider-heading" style="left:0;right:0;top:100px;text-align:center">This is your divider page</div>
</section>

<section class="slide">
  <div class="slide-title">Quote Area</div>
  <div class="box-green" style="left:0;top:80px;width:220px;height:110px"></div>
  <div class="photo photo--sky" style="left:220px;top:50px;width:176px;height:140px" role="img" aria-label="House with front garden"></div>
  <p class="abs" style="left:20px;top:104px;width:180px;font-size:8px;font-style:italic;color:var(--white);line-height:1.5">“A home is the best investment a family can make.”</p>
  <span class="brand-foot">VELMIRA</span>
</section>

<section class="slide">
  <div class="slide-title">Brand Detailed</div>
  <div class="photo photo--sky" style="left:16px;top:40px;width:220px;height:160px" role="img" aria-label="Residential building facade"></div>
  <div class="box-green" style="left:250px;top:40px;width:130px;height:50px"></div>
  <div class="box-brown" style="left:250px;top:96px;width:130px;height:50px"></div>
  <div class="box-green" style="left:250px;top:152px;width:130px;height:48px"></div>
  <div class="abs label label--light" style="left:262px;top:60px">Quality</div>
  <div class="abs label label--light" style="left:262px;top:116px">Trust</div>
  <div class="abs label label--light" style="left:262px;top:171px">Value</div>
</section>

<!-- row 8 -->
<section class="slide">
  <div class="slide-title">Product Philosophy</div>
  <svg class="abs" style="left:130px;top:36px" width="140" height="170" viewBox="0 0 140 170">
    <circle cx="70" cy="90" r="48" fill="none" stroke="var(--green)" stroke-width="10"/>
    <circle cx="70" cy="90" r="24" fill="var(--green)"/>
    <circle cx="70" cy="30" r="12" fill="var(--brown)"/><circle cx="130" cy="90" r="12" fill="var(--green-deep)"/>
    <circle cx="70" cy="150" r="12" fill="var(--brown)"/><circle cx="10" cy="90" r="12" fill="var(--green-deep)"/>
  </svg>
  <div class="abs label" style="left:20px;top:80px">Design</div><div class="abs label" style="left:20px;top:150px">Build</div>
  <div class="abs label" style="left:300px;top:80px">Sell</div><div class="abs label" style="left:300px;top:150px">Deliver</div>
  <span class="brand-foot">VELMIRA</span>
</section>

<section class="slide slide--grey">
  <div class="slide-title">Apartments per Year</div>
  <svg class="abs" style="left:30px;top:40px" width="340" height="170" viewBox="0 0 340 170">
    <g fill="var(--green)">
      <rect x="0" y="80" width="30" height="70"/><rect x="48" y="60" width="30" height="90"/><rect x="96" y="100" width="30" height="50"/>
      <rect x="144" y="40" width="30" height="110"/><rect x="192" y="70" width="30" height="80"/><rect x="240" y="20" width="30" height="130"/><rect x="288" y="50" width="30" height="100"/>
    </g>
    <g font-size="6" fill="var(--muted)" text-anchor="middle"><text x="15" y="162">2012</text><text x="63" y="162">2013</text><text x="111" y="162">2014</text><text x="159" y="162">2015</text><text x="207" y="162">2016</text><text x="255" y="162">2017</text><text x="303" y="162">2018</text></g>
  </svg>
  <span class="brand-foot">VELMIRA</span>
</section>

<section class="slide">
  <div class="slide-title">Trending in the World</div>
  <div class="photo photo--green" style="left:20px;top:40px;width:220px;height:140px;opacity:.55" role="img" aria-label="World map"></div>
  <svg class="abs" style="left:270px;top:40px" width="100" height="150" viewBox="0 0 100 150">
    <circle cx="50" cy="35" r="28" fill="none" stroke="var(--grey-mid)" stroke-width="7"/>
    <circle cx="50" cy="35" r="28" fill="none" stroke="var(--green)" stroke-width="7" stroke-dasharray="123 176" transform="rotate(-90 50 35)"/>
    <text x="50" y="39" text-anchor="middle" font-size="11" font-weight="700" fill="var(--ink)">70%</text>
    <circle cx="50" cy="110" r="28" fill="none" stroke="var(--grey-mid)" stroke-width="7"/>
    <circle cx="50" cy="110" r="28" fill="none" stroke="var(--brown)" stroke-width="7" stroke-dasharray="88 176" transform="rotate(-90 50 110)"/>
    <text x="50" y="114" text-anchor="middle" font-size="11" font-weight="700" fill="var(--ink)">50%</text>
  </svg>
  <span class="brand-foot">VELMIRA</span>
</section>

<!-- row 9 -->
<section class="slide">
  <div class="slide-title">Peru Map</div>
  <div class="photo photo--green" style="left:30px;top:40px;width:130px;height:160px;opacity:.6" role="img" aria-label="Map of Peru with Lima highlighted"></div>
  <div class="abs" style="left:190px;top:60px;width:180px">
    <div class="label">Lima, capital of Peru</div>
    <p class="note" style="margin-top:6px">Home to one third of the country's population and the largest demand for new housing.</p>
  </div>
  <span class="brand-foot">VELMIRA</span>
</section>

<section class="slide">
  <div class="slide-title">Population vs Housing in Peru</div>
  <svg class="abs" style="left:20px;top:60px" width="260" height="110" viewBox="0 0 260 110">
    <g fill="var(--brown)"><rect x="0" y="0" width="14" height="30"/><rect x="22" y="0" width="14" height="30"/><rect x="44" y="0" width="14" height="30"/><rect x="66" y="0" width="14" height="30"/><rect x="88" y="0" width="14" height="30"/><rect x="110" y="0" width="14" height="30"/><rect x="132" y="0" width="14" height="30"/><rect x="154" y="0" width="14" height="30"/><rect x="176" y="0" width="14" height="30"/><rect x="198" y="0" width="14" height="30"/></g>
    <g fill="var(--green)"><rect x="0" y="60" width="14" height="30"/><rect x="22" y="60" width="14" height="30"/><rect x="44" y="60" width="14" height="30"/><rect x="66" y="60" width="14" height="30"/><rect x="88" y="60" width="14" height="30"/><rect x="110" y="60" width="14" height="30"/><rect x="132" y="60" width="14" height="30"/></g>
    <g fill="var(--grey-mid)"><rect x="154" y="60" width="14" height="30"/><rect x="176" y="60" width="14" height="30"/><rect x="198" y="60" width="14" height="30"/></g>
  </svg>
  <div class="abs" style="left:290px;top:60px;font-size:16px;font-weight:800;color:var(--brown)">15,2M</div>
  <div class="abs big-stat" style="left:290px;top:120px;font-size:16px">11,7M</div>
  <span class="brand-foot">VELMIRA</span>
</section>

<section class="slide slide--brown">
  <div class="slide-title slide-title--light">Our Vision &amp; Mission</div>
  <div class="box-green" style="left:20px;top:60px;width:170px;height:3px"></div>
  <div class="box-green" style="left:206px;top:60px;width:170px;height:3px"></div>
  <div class="abs" style="left:20px;top:72px;width:170px"><div class="label label--light">Our Vision</div><p class="note note--light" style="margin-top:5px">To be the leading middle income housing developer in Peru.</p></div>
  <div class="abs" style="left:206px;top:72px;width:170px"><div class="label label--light">Our Mission</div><p class="note note--light" style="margin-top:5px">Deliver quality homes and strong returns to our investors.</p></div>
  <span class="brand-foot brand-foot--light">VELMIRA</span>
</section>

<!-- row 10 -->
<section class="slide">
  <div class="slide-title">Our Services</div>
  <div class="photo photo--dark" style="left:16px;top:40px;width:150px;height:110px" role="img" aria-label="Construction site"></div>
  <div class="abs" style="left:184px;top:44px;width:190px;display:grid;gap:10px">
    <div><div class="label">Development</div><p class="note">Land, permits and design.</p></div>
    <div><div class="label">Construction</div><p class="note">Quality vertical housing.</p></div>
    <div><div class="label">Sales &amp; Marketing</div><p class="note">In-house commercial team.</p></div>
  </div>
  <span class="brand-foot">VELMIRA</span>
</section>

<section class="slide">
  <div class="slide-title">Three Column Description</div>
  <div class="abs" style="left:20px;top:56px;width:356px;display:grid;grid-template-columns:repeat(3,1fr);gap:16px">
    <div><div class="box-green" style="position:static;width:24px;height:3px;margin-bottom:6px"></div><div class="label">Delivered</div><p class="note">1,400 apartments handed over to families.</p></div>
    <div><div class="box-green" style="position:static;width:24px;height:3px;margin-bottom:6px"></div><div class="label">Building</div><p class="note">400 apartments under construction today.</p></div>
    <div><div class="box-green" style="position:static;width:24px;height:3px;margin-bottom:6px"></div><div class="label">Pipeline</div><p class="note">1,500 more apartments ready to develop.</p></div>
  </div>
  <span class="brand-foot">VELMIRA</span>
</section>

<section class="slide">
  <div class="slide-title">Our Team</div>
  <div class="photo photo--warm photo--round" style="left:170px;top:50px;width:56px;height:56px;border:3px solid var(--green)" role="img" aria-label="Portrait of the general manager"></div>
  <div class="abs label" style="left:0;right:0;top:118px;text-align:center">General Manager</div>
  <p class="abs note" style="left:110px;width:176px;top:132px;text-align:center">Twenty years leading housing projects in Lima.</p>
  <span class="brand-foot">VELMIRA</span>
</section>

<!-- row 11 -->
<section class="slide slide--green">
  <div class="photo photo--green" style="left:0;top:0;width:396px;height:223px" role="img" aria-label="Residential building in green tones"></div>
  <div class="abs divider-heading" style="left:0;right:0;top:104px;text-align:center">This is your divider page</div>
</section>

<section class="slide">
  <div class="abs" style="left:0;right:0;top:14px;text-align:center;font-size:10px;font-weight:700;text-transform:uppercase">Monthly Subscription</div>
  <div class="price-col" style="left:40px"><header>Basic</header><div class="amount">$50</div><p>Project report<br>Quarterly call<br>Site visit</p></div>
  <div class="price-col" style="left:152px;top:42px;height:158px;background:var(--brown)"><header>Standard</header><div class="amount" style="color:var(--white)">$90</div><p style="color:#ddd">Project report<br>Monthly call<br>Site visit</p></div>
  <div class="price-col" style="left:264px"><header>Premium</header><div class="amount">$150</div><p>Full reports<br>Weekly call<br>Site visits</p></div>
</section>

<section class="slide">
  <div class="slide-title">Your Title Goes Here</div>
  <table class="table" style="left:30px;top:40px;width:336px">
    <tr><th>Project</th><th>District</th><th>Units</th><th>Status</th></tr>
    <tr><td>Torre Norte</td><td>Surco</td><td>120</td><td>Delivered</td></tr>
    <tr><td>Parque Sol</td><td>San Miguel</td><td>180</td><td>Delivered</td></tr>
    <tr><td>Vista Lima</td><td>Lince</td><td>150</td><td>Building</td></tr>
    <tr><td>Los Olivos</td><td>Breña</td><td>250</td><td>Building</td></tr>
    <tr><td>Jardines</td><td>Ate</td><td>300</td><td>Pipeline</td></tr>
    <tr><td>Mirador</td><td>Callao</td><td>220</td><td>Pipeline</td></tr>
  </table>
  <span class="brand-foot">VELMIRA</span>
</section>

<!-- row 12 -->
<section class="slide">
  <div class="slide-title">Our Team</div>
  <div class="photo photo--warm photo--round" style="left:40px;top:48px;width:40px;height:40px" role="img" aria-label="Team member portrait"></div>
  <div class="abs" style="left:90px;top:56px"><div class="label">Director</div><p class="note">Finance</p></div>
  <div class="photo photo--warm photo--round" style="left:220px;top:48px;width:40px;height:40px" role="img" aria-label="Team member portrait"></div>
  <div class="abs" style="left:270px;top:56px"><div class="label">Director</div><p class="note">Operations</p></div>
  <div class="photo photo--warm photo--round" style="left:40px;top:120px;width:40px;height:40px" role="img" aria-label="Team member portrait"></div>
  <div class="abs" style="left:90px;top:128px"><div class="label">Manager</div><p class="note">Sales</p></div>
  <div class="photo photo--warm photo--round" style="left:220px;top:120px;width:40px;height:40px" role="img" aria-label="Team member portrait"></div>
  <div class="abs" style="left:270px;top:128px"><div class="label">Manager</div><p class="note">Projects</p></div>
  <span class="brand-foot">VELMIRA</span>
</section>

<section class="slide">
  <div class="slide-title">Customer Testimonials</div>
  <div class="abs" style="left:20px;top:50px;width:356px;display:grid;grid-template-columns:repeat(3,1fr);gap:14px;text-align:center">
    <div><div class="photo photo--warm photo--round" style="position:relative;width:34px;height:34px;margin:0 auto 8px" role="img" aria-label="Customer portrait"></div><p class="note">“Our new home arrived on time.”</p></div>
    <div><div class="photo photo--warm photo--round" style="position:relative;width:34px;height:34px;margin:0 auto 8px" role="img" aria-label="Customer portrait"></div><p class="note">“Great quality for the price.”</p></div>
    <div><div class="photo photo--warm photo--round" style="position:relative;width:34px;height:34px;margin:0 auto 8px" role="img" aria-label="Customer portrait"></div><p class="note">“A safe place for our kids.”</p></div>
  </div>
  <span class="brand-foot">VELMIRA</span>
</section>

<section class="slide">
  <div class="slide-title">Two Pictures Slide</div>
  <div class="photo photo--sky" style="left:16px;top:40px;width:176px;height:140px" role="img" aria-label="Apartment building"></div>
  <div class="photo" style="left:204px;top:40px;width:176px;height:140px" role="img" aria-label="House exterior"></div>
  <span class="brand-foot">VELMIRA</span>
</section>

<!-- row 13 -->
<section class="slide">
  <div class="slide-title">Title and Image + Text</div>
  <div class="photo photo--dark" style="left:16px;top:36px;width:364px;height:100px" role="img" aria-label="Lima skyline at night"></div>
  <div class="abs" style="left:16px;top:148px;width:364px;display:grid;grid-template-columns:1fr 1fr;gap:16px">
    <p class="note">Lima concentrates the largest housing deficit in South America's Pacific capitals.</p>
    <p class="note">Middle income families drive demand for new vertical housing.</p>
  </div>
  <span class="brand-foot">VELMIRA</span>
</section>

<section class="slide">
  <div class="slide-title slide-title--case">Home Improvements</div>
  <div class="photo photo--green" style="left:176px;top:34px;width:196px;height:159px;opacity:.8" role="img" aria-label="Illustrated house cut away to show its rooms"></div>
  <div class="abs" style="left:16px;top:40px;width:140px;display:grid;gap:9px">
    <div><div class="row" style="justify-content:space-between"><span class="label label--green">Kitchen</span><span class="label">45%</span></div><div class="meter"><i style="width:45%"></i></div></div>
    <div><div class="row" style="justify-content:space-between"><span class="label label--green">Bedrooms</span><span class="label">70%</span></div><div class="meter"><i style="width:70%"></i></div></div>
    <div><div class="row" style="justify-content:space-between"><span class="label label--green">Bathrooms</span><span class="label">35%</span></div><div class="meter"><i style="width:35%"></i></div></div>
    <div><div class="row" style="justify-content:space-between"><span class="label label--green">Living room</span><span class="label">60%</span></div><div class="meter"><i style="width:60%"></i></div></div>
  </div>
  <div class="ground"></div>
  <div class="ground-legend"><span>Finishes upgraded</span><span>Share of units, 2018</span></div>
</section>

<section class="slide">
  <div class="slide-title slide-title--case">Building Infographic</div>
  <div class="photo photo--soft" style="left:0;top:44px;width:396px;height:149px" role="img" aria-label="Faint city skyline of apartment blocks"></div>
  <svg class="abs" style="left:20px;top:50px" width="356" height="143" viewBox="0 0 356 143">
    <g font-size="6" font-weight="700" text-anchor="middle">
      <rect x="0" y="70" width="26" height="73" fill="var(--brown)"/><text x="13" y="64" fill="var(--brown)">120</text>
      <rect x="36" y="50" width="26" height="93" fill="var(--green)"/><text x="49" y="44" fill="var(--green-deep)">180</text>
      <rect x="72" y="90" width="26" height="53" fill="var(--brown)"/><text x="85" y="84" fill="var(--brown)">90</text>
      <rect x="108" y="35" width="26" height="108" fill="var(--green)"/><text x="121" y="29" fill="var(--green-deep)">210</text>
      <rect x="144" y="60" width="26" height="83" fill="var(--brown)"/><text x="157" y="54" fill="var(--brown)">150</text>
      <rect x="180" y="25" width="26" height="118" fill="var(--green)"/><text x="193" y="19" fill="var(--green-deep)">240</text>
      <rect x="216" y="80" width="26" height="63" fill="var(--brown)"/><text x="229" y="74" fill="var(--brown)">110</text>
      <rect x="252" y="40" width="26" height="103" fill="var(--green)"/><text x="265" y="34" fill="var(--green-deep)">200</text>
      <rect x="288" y="65" width="26" height="78" fill="var(--brown)"/><text x="301" y="59" fill="var(--brown)">140</text>
      <rect x="324" y="10" width="26" height="133" fill="var(--green)"/><text x="337" y="6" fill="var(--green-deep)">260</text>
    </g>
  </svg>
  <div class="ground"></div>
  <div class="ground-legend"><span>■ Delivered</span><span>■ Pipeline</span><span>Units per project</span></div>
</section>

<!-- row 14 -->
<section class="slide">
  <div class="slide-title slide-title--case">Property Infographic</div>
  <div class="photo photo--dark" style="left:16px;top:60px;width:160px;height:90px;border-radius:45px 8px 8px 45px" role="img" aria-label="Illustrated bunch of house keys"></div>
  <div class="abs big-stat" style="left:196px;top:54px;font-size:22px">35%</div>
  <p class="abs note" style="left:196px;top:82px;width:80px">Of buyers are first-time owners.</p>
  <div class="abs" style="left:290px;top:50px;width:90px;display:grid;gap:10px">
    <div><span class="label">Presale</span><div class="meter"><i style="width:85%"></i></div></div>
    <div><span class="label">Mortgage</span><div class="meter"><i style="width:60%"></i></div></div>
    <div><span class="label">Cash</span><div class="meter"><i style="width:25%"></i></div></div>
  </div>
  <p class="abs note" style="left:196px;top:120px;width:184px">85% of units are sold before construction ends, lowering investor risk.</p>
  <span class="brand-foot">VELMIRA</span>
</section>

<section class="slide">
  <div class="slide-title slide-title--case">House Infographic</div>
  <div class="photo photo--soft" style="left:0;top:40px;width:396px;height:153px" role="img" aria-label="Faint row of grey houses"></div>
  <svg class="abs" style="left:30px;top:40px" width="340" height="153" viewBox="0 0 340 153">
    <g fill="var(--grey-dark)"><rect x="0" y="93" width="40" height="60"/><rect x="120" y="73" width="40" height="80"/><rect x="240" y="83" width="40" height="70"/></g>
    <g fill="var(--green)"><rect x="60" y="53" width="40" height="100"/><rect x="180" y="33" width="40" height="120"/><rect x="300" y="13" width="40" height="140"/></g>
    <g font-size="7" font-weight="700" text-anchor="middle"><text x="80" y="48" fill="var(--green-deep)">40%</text><text x="200" y="28" fill="var(--green-deep)">55%</text><text x="320" y="9" fill="var(--green-deep)">70%</text></g>
  </svg>
  <div class="ground"></div>
  <div class="ground-legend"><span>2016</span><span>2017</span><span>2018</span></div>
</section>

<section class="slide">
  <div class="slide-title slide-title--case">Construction Infographic</div>
  <div class="photo photo--warm" style="left:16px;top:34px;width:180px;height:159px;opacity:.85" role="img" aria-label="Illustrated tower crane over a building"></div>
  <svg class="abs" style="left:210px;top:60px" width="170" height="133" viewBox="0 0 170 133">
    <g fill="var(--green)"><rect x="0" y="60" width="22" height="73"/><rect x="50" y="30" width="22" height="103"/><rect x="100" y="5" width="22" height="128"/></g>
    <g fill="var(--brown)"><rect x="24" y="80" width="22" height="53"/><rect x="74" y="55" width="22" height="78"/><rect x="124" y="40" width="22" height="93"/></g>
  </svg>
  <div class="abs" style="left:210px;top:36px"><span class="label">400 units</span> <span class="note">under construction</span></div>
  <div class="ground"></div>
  <div class="ground-legend"><span>■ Structure</span><span>■ Finishes</span></div>
</section>

<!-- row 15 -->
<section class="slide">
  <div class="slide-title slide-title--case">Construction Infographic</div>
  <div class="photo photo--green" style="left:16px;top:120px;width:364px;height:73px;opacity:.6" role="img" aria-label="Illustrated construction trucks on site"></div>
  <div class="stat-block" style="left:16px;top:40px"><b>1,400</b><span>Apartments delivered</span></div>
  <div class="stat-block" style="left:108px;top:40px"><b>400</b><span>Under construction</span></div>
  <div class="stat-block" style="left:200px;top:40px"><b>1,500</b><span>Units in pipeline</span></div>
  <div class="stat-block" style="left:292px;top:40px"><b style="color:var(--brown)">US$60mm</b><span>Yearly raise target</span></div>
  <div class="ground"></div>
  <div class="ground-legend"><span>Lima</span><span>Project progress</span></div>
</section>

<section class="slide">
  <div class="slide-title slide-title--case">Apartment Infographic</div>
  <svg class="abs" style="left:30px;top:34px" width="340" height="159" viewBox="0 0 340 159">
    <g fill="var(--brown-soft)"><rect x="0" y="114" width="30" height="45"/><rect x="90" y="94" width="30" height="65"/><rect x="180" y="104" width="30" height="55"/><rect x="270" y="84" width="30" height="75"/></g>
    <g fill="var(--green)"><rect x="40" y="74" width="30" height="85"/><rect x="130" y="44" width="30" height="115"/><rect x="220" y="54" width="30" height="105"/><rect x="310" y="14" width="30" height="145"/></g>
    <g font-size="7" font-weight="700" text-anchor="middle" fill="var(--green-deep)"><text x="55" y="69">85</text><text x="145" y="39">115</text><text x="235" y="49">105</text><text x="325" y="10">145</text></g>
  </svg>
  <div class="ground"></div>
  <div class="ground-legend"><span>Q1</span><span>Q2</span><span>Q3</span><span>Q4</span></div>
</section>

<section class="slide">
  <div class="slide-title slide-title--case">House Infographic</div>
  <div class="photo photo--dark" style="left:16px;top:110px;width:364px;height:83px;opacity:.55" role="img" aria-label="Illustrated row of houses on green hills"></div>
  <svg class="abs" style="left:30px;top:40px" width="340" height="66" viewBox="0 0 340 66">
    <g font-size="7" font-weight="700" fill="var(--ink)"><text x="0" y="8">Surco</text><text x="0" y="30">Lince</text><text x="0" y="52">Ate</text></g>
    <rect x="50" y="2" width="260" height="8" fill="var(--grey-mid)"/><rect x="50" y="2" width="210" height="8" fill="var(--green)"/>
    <rect x="50" y="24" width="260" height="8" fill="var(--grey-mid)"/><rect x="50" y="24" width="150" height="8" fill="var(--brown)"/>
    <rect x="50" y="46" width="260" height="8" fill="var(--grey-mid)"/><rect x="50" y="46" width="120" height="8" fill="var(--green)"/>
    <g font-size="7" font-weight="700" fill="var(--green-deep)"><text x="318" y="9">80%</text><text x="318" y="31">58%</text><text x="318" y="53">46%</text></g>
  </svg>
  <div class="ground ground--green"></div>
  <div class="ground-legend"><span>Sold per district</span><span>2018</span></div>
</section>

<!-- row 16 -->
<section class="slide">
  <div class="slide-title slide-title--case">Eviction Infographic</div>
  <div class="photo photo--dark" style="left:16px;top:90px;width:150px;height:103px;opacity:.8" role="img" aria-label="Illustrated bulldozer clearing a lot"></div>
  <svg class="abs" style="left:186px;top:40px" width="190" height="153" viewBox="0 0 190 153">
    <g fill="var(--grey-dark)"><rect x="0" y="70" width="28" height="83"/><rect x="80" y="95" width="28" height="58"/></g>
    <g fill="var(--green)"><rect x="40" y="30" width="28" height="123"/><rect x="120" y="10" width="28" height="143"/></g>
    <rect x="160" y="55" width="28" height="98" fill="var(--brown)"/>
  </svg>
  <div class="abs" style="left:16px;top:40px;width:150px"><div class="label">Land renewal</div><p class="note" style="margin-top:4px">Old lots cleared and rebuilt as new family apartments.</p></div>
  <div class="ground"></div>
  <div class="ground-legend"><span>Before</span><span>After</span></div>
</section>

<section class="slide">
  <div class="slide-title slide-title--case">Urban Growth</div>
  <svg class="abs" style="left:30px;top:40px" width="340" height="153" viewBox="0 0 340 153">
    <g fill="var(--green)"><rect x="0" y="93" width="34" height="60"/><rect x="50" y="63" width="34" height="90"/><rect x="100" y="103" width="34" height="50"/><rect x="150" y="33" width="34" height="120"/><rect x="200" y="73" width="34" height="80"/><rect x="250" y="13" width="34" height="140"/><rect x="300" y="53" width="34" height="100"/></g>
    <g font-size="7" font-weight="700" text-anchor="middle" fill="var(--green-deep)"><text x="17" y="88">3%</text><text x="67" y="58">5%</text><text x="117" y="98">2%</text><text x="167" y="28">7%</text><text x="217" y="68">4%</text><text x="267" y="9">8%</text><text x="317" y="48">6%</text></g>
  </svg>
  <div class="ground"></div>
  <div class="ground-legend"><span>2012</span><span>2014</span><span>2016</span><span>2018</span></div>
</section>

<section class="slide">
  <div class="slide-title">Sales Comparison</div>
  <div class="abs big-stat" style="left:24px;top:60px;font-size:20px">45%</div>
  <p class="abs note" style="left:24px;top:88px">Lima</p>
  <div class="abs" style="left:24px;top:120px;font-size:20px;font-weight:800;color:var(--brown)">65%</div>
  <p class="abs note" style="left:24px;top:148px">Other capitals</p>
  <svg class="abs" style="left:130px;top:50px" width="250" height="150" viewBox="0 0 250 150">
    <g fill="var(--green)"><rect x="0" y="60" width="24" height="80"/><rect x="60" y="40" width="24" height="100"/><rect x="120" y="70" width="24" height="70"/><rect x="180" y="30" width="24" height="110"/></g>
    <g fill="var(--brown)"><rect x="26" y="80" width="24" height="60"/><rect x="86" y="50" width="24" height="90"/><rect x="146" y="90" width="24" height="50"/><rect x="206" y="60" width="24" height="80"/></g>
    <g font-size="6" fill="var(--muted)" text-anchor="middle"><text x="25" y="149">Lima</text><text x="85" y="149">Bogotá</text><text x="145" y="149">Santiago</text><text x="205" y="149">Quito</text></g>
  </svg>
  <span class="brand-foot">VELMIRA</span>
</section>

<!-- row 17 -->
<section class="slide">
  <div class="photo photo--dark" style="left:0;top:0;width:396px;height:223px" role="img" aria-label="Apartment building at night"></div>
  <div class="abs divider-heading" style="left:0;right:0;top:100px;text-align:center;font-size:11px">Your Title Goes Here</div>
</section>

<section class="slide">
  <div class="logo-lockup" style="left:150px;top:40px"><span class="logo-square" style="width:12px;height:12px"></span><span class="logo-name" style="font-size:16px">VELMIRA</span></div>
  <div class="box-brown" style="left:0;top:110px;width:396px;height:50px"></div>
  <div class="abs divider-heading" style="left:0;right:0;top:126px;text-align:center;font-size:11px">This is your timeline page</div>
</section>

<section class="slide">
  <div class="slide-title">Your Title</div>
  <div class="box-green" style="left:0;top:40px;width:170px;height:160px"></div>
  <p class="abs note note--light" style="left:16px;top:60px;width:140px">Investors share in the returns of each project through fees aligned to IRR.</p>
  <div class="photo photo--sky" style="left:180px;top:40px;width:216px;height:160px" role="img" aria-label="Residential courtyard with pool"></div>
</section>

<!-- row 18 -->
<section class="slide">
  <div class="slide-title">Your Title</div>
  <div class="photo photo--warm" style="left:16px;top:40px;width:170px;height:150px" role="img" aria-label="Brick apartment building"></div>
  <div class="abs" style="left:204px;top:50px;width:170px"><div class="label">Proven developer</div><p class="note" style="margin-top:6px">Years of experience building middle income apartments in Lima's growing districts.</p></div>
  <span class="brand-foot">VELMIRA</span>
</section>

<section class="slide">
  <svg class="abs" style="left:186px;top:0" width="24" height="223" viewBox="0 0 24 223">
    <line x1="12" y1="0" x2="12" y2="223" stroke="var(--grey-mid)" stroke-width="2"/>
    <circle cx="12" cy="50" r="7" fill="var(--green)"/><circle cx="12" cy="120" r="7" fill="var(--brown)"/><circle cx="12" cy="190" r="7" fill="var(--green)"/>
  </svg>
  <div class="abs big-stat" style="left:222px;top:42px;font-size:14px">85%</div>
  <div class="abs label" style="left:110px;top:116px">Your Title Here</div>
  <p class="abs note" style="left:222px;top:184px">Project launch</p>
</section>

<section class="slide">
  <div class="slide-title">Who We Are?</div>
  <div class="abs" style="left:20px;top:46px;width:180px;display:grid;gap:8px">
    <div class="row"><span class="dot" style="width:6px;height:6px"></span><span class="note">Peruvian real estate developer</span></div>
    <div class="row"><span class="dot" style="width:6px;height:6px"></span><span class="note">Focused on vertical housing</span></div>
    <div class="row"><span class="dot" style="width:6px;height:6px"></span><span class="note">1,400 apartments delivered</span></div>
    <div class="row"><span class="dot" style="width:6px;height:6px"></span><span class="note">Raising US$50–60mm per year</span></div>
  </div>
  <div class="photo photo--warm" style="left:220px;top:40px;width:160px;height:150px" role="img" aria-label="Team on a building site"></div>
  <span class="brand-foot">VELMIRA</span>
</section>

<!-- row 19 -->
<section class="slide">
  <div class="slide-title">Three Steps</div>
  <svg class="abs" style="left:150px;top:36px" width="100" height="170" viewBox="0 0 100 170">
    <circle cx="50" cy="30" r="24" fill="none" stroke="var(--green)" stroke-width="10"/>
    <circle cx="50" cy="85" r="24" fill="none" stroke="var(--green-deep)" stroke-width="10"/>
    <circle cx="50" cy="140" r="24" fill="none" stroke="var(--green)" stroke-width="10"/>
  </svg>
  <div class="abs label" style="left:40px;top:62px">Invest</div>
  <div class="abs label" style="left:280px;top:117px">Build</div>
  <div class="abs label" style="left:40px;top:172px">Return</div>
  <span class="brand-foot">VELMIRA</span>
</section>

<section class="slide">
  <svg class="abs" style="left:186px;top:0" width="24" height="223" viewBox="0 0 24 223">
    <line x1="12" y1="0" x2="12" y2="223" stroke="var(--grey-mid)" stroke-width="2"/>
    <circle cx="12" cy="40" r="7" fill="var(--brown)"/><circle cx="12" cy="110" r="7" fill="var(--green)"/><circle cx="12" cy="180" r="7" fill="var(--brown)"/>
  </svg>
  <p class="abs note" style="left:222px;top:36px">Construction starts</p>
  <p class="abs note" style="left:120px;top:106px">Sales launch</p>
  <p class="abs note" style="left:222px;top:176px">Keys delivered</p>
</section>

<section class="slide">
  <div class="slide-title">Project Timeline</div>
  <svg class="abs" style="left:20px;top:40px" width="356" height="160" viewBox="0 0 356 160">
    <g stroke="var(--grey-mid)"><line x1="80" y1="0" x2="80" y2="160"/><line x1="150" y1="0" x2="150" y2="160"/><line x1="220" y1="0" x2="220" y2="160"/><line x1="290" y1="0" x2="290" y2="160"/></g>
    <g font-size="6" fill="var(--ink)"><text x="0" y="18">Land</text><text x="0" y="48">Permits</text><text x="0" y="78">Design</text><text x="0" y="108">Build</text><text x="0" y="138">Sales</text></g>
    <rect x="80" y="10" width="60" height="12" fill="var(--green)"/>
    <rect x="120" y="40" width="70" height="12" fill="var(--brown)"/>
    <rect x="150" y="70" width="80" height="12" fill="var(--green)"/>
    <rect x="200" y="100" width="140" height="12" fill="var(--brown)"/>
    <rect x="180" y="130" width="160" height="12" fill="var(--green)"/>
  </svg>
  <span class="brand-foot">VELMIRA</span>
</section>

<!-- row 20 -->
<section class="slide">
  <div class="photo" style="left:0;top:0;width:170px;height:223px" role="img" aria-label="Historic building facade"></div>
  <div class="box-brown" style="left:170px;top:0;width:226px;height:223px"></div>
  <div class="abs label label--light" style="left:190px;top:40px;font-size:9px">Key Points</div>
  <div class="abs" style="left:190px;top:64px;width:180px;display:grid;gap:8px">
    <div class="row"><span class="dot" style="width:6px;height:6px"></span><span class="note note--light">Strong housing demand</span></div>
    <div class="row"><span class="dot" style="width:6px;height:6px"></span><span class="note note--light">Experienced developer</span></div>
    <div class="row"><span class="dot" style="width:6px;height:6px"></span><span class="note note--light">Returns aligned to IRR</span></div>
  </div>
</section>

<section class="slide">
  <div class="slide-title">Three Bullets Area</div>
  <div class="abs" style="left:20px;top:40px;width:356px;display:grid;grid-template-columns:repeat(3,1fr);gap:14px">
    <div><div class="label label--green">01</div><p class="note">Management fees</p></div>
    <div><div class="label label--green">02</div><p class="note">Sales fees</p></div>
    <div><div class="label label--green">03</div><p class="note">Success fees</p></div>
  </div>
  <div class="photo photo--sky" style="left:0;top:100px;width:396px;height:123px" role="img" aria-label="Row of residential buildings"></div>
</section>

<section class="slide slide--green">
  <div class="photo photo--green" style="left:0;top:0;width:396px;height:223px" role="img" aria-label="Apartment building in green tones"></div>
  <div class="abs" style="right:24px;top:88px;text-align:right">
    <div style="font-size:20px;font-weight:800;color:var(--white)">THANK YOU</div>
    <p class="note note--light" style="margin-top:4px">For your attention</p>
  </div>
</section>

</main>
</body>
</html>
```